FAST TURN AROUND - Yoga & Sound Meditation Event Flyer

Our organization - Tarrow Guidance Alliance - is currently looking for someone to create a flyer for an upcoming Yoga & Sound Meditation Event.

We are looking for the following deliverables:
Versions of the Flyer created for Social Media (Long Story & Square Post) that includes the following information. (Not including the categories)
Event Title: Tarrow Flow & Hum Unwind Session - Bayline Mix
Event Date & Time: Wednesday, April 20 | 7P - 9P
Event Location: Reedhall at Cobbleyard
Tarrow Logo: (Both black and white versions are attached. Feel free to use whichever makes more sense based on the lighting)

We would want a version of this for the eight different background images provided. For the test, you can submit 1-2 since the rest of the details will be the same once we chose the information design.

```html
<!DOCTYPE html>
<html lang="en">
<head>
<meta charset="utf-8">
<title>Tarrow Flow &amp; Hum Unwind Session – Flyers</title>
<link href="https://fonts.googleapis.com/css2?family=Montserrat:ital,wght@0,800;1,800&family=Quicksand:wght@500&family=Lato:wght@400&family=Arimo:wght@400&display=swap" rel="stylesheet">
<style>
  :root {
    --stage: #262626;
    --navy: #1a1c8f;
    --royal: #1a3fd6;
    --glow: #2f7bff;
    --ink: #000000;
    --white: #ffffff;
    --word-solid: #e9eef8;
    --word-grey: rgba(200, 206, 214, 0.62);
    --ring: rgba(150, 205, 255, 0.55);
    --photo-top: #5a4a44;
    --photo-mid: #cbbdb6;
    --photo-low: #2a2424;
  }
  * { margin: 0; padding: 0; box-sizing: border-box; }
  html, body { width: 1200px; height: 1200px; overflow: hidden; background: var(--stage); }
  .stage { position: relative; width: 1200px; height: 1200px; }

  .flyer {
    position: absolute;
    overflow: hidden;
    background:
      linear-gradient(to bottom, transparent 62%, rgba(0,0,0,0.55) 82%, var(--ink) 96%),
      radial-gradient(ellipse 70% 55% at 50% 48%, var(--glow) 0%, var(--royal) 45%, var(--navy) 100%);
    color: var(--white);
    text-align: center;
  }
  .flyer--square { left: 84px; top: 363px; width: 476px; height: 476px; }
  .flyer--story  { left: 600px; top: 215px; width: 518px; height: 670px; }

  .flyer__pattern {
    position: absolute; inset: 0;
    background: radial-gradient(circle at 50% 42%, rgba(90,140,255,0.25) 0%, rgba(40,70,220,0.1) 50%, transparent 75%);
  }
  .flyer__rings, .flyer__words { position: absolute; left: 0; top: 0; width: 100%; height: 100%; }

  .flyer__line { position: absolute; left: 0; width: 100%; white-space: nowrap; line-height: 1; }
  .brand { font-family: "Montserrat", sans-serif; font-weight: 800; letter-spacing: -0.5px; }
  .brand-sub { font-family: "Lato", sans-serif; font-weight: 400; }
  .event-title { font-family: "Montserrat", sans-serif; font-weight: 800; font-style: italic; }
  .event-mix { font-family: "Quicksand", sans-serif; font-weight: 500; letter-spacing: 1px; }
  .event-date { font-family: "Quicksand", sans-serif; font-weight: 500; letter-spacing: 0.3px; }
  .event-venue { font-family: "Arimo", sans-serif; font-weight: 400; }
  .event-venue svg { vertical-align: -2px; margin-right: 6px; }

  .big-word { font-family: "Montserrat", sans-serif; font-weight: 800; }

  .flyer__portrait {
    position: absolute;
    background: linear-gradient(to bottom, var(--photo-top) 0%, var(--photo-mid) 28%, var(--photo-mid) 88%, var(--photo-low) 100%);
    border-radius: 40% 40% 6px 6px / 16% 16% 0 0;
  }
</style>
</head>
<body>
<main class="stage">

  <!-- Square post -->
  <section class="flyer flyer--square">
    <div class="flyer__pattern" role="img" aria-label="Blue mandala line pattern background"></div>
    <svg class="flyer__rings" viewBox="0 0 476 476" aria-hidden="true">
      <g fill="none" stroke="var(--ring)" stroke-width="1.5">
        <ellipse cx="238" cy="320" rx="90" ry="120"/>
        <ellipse cx="238" cy="320" rx="150" ry="170"/>
        <ellipse cx="238" cy="320" rx="215" ry="220"/>
        <ellipse cx="238" cy="320" rx="285" ry="270"/>
      </g>
    </svg>
    <svg class="flyer__words" viewBox="0 0 476 476" aria-hidden="true">
      <text class="big-word" x="4" y="312" font-size="92" textLength="468" lengthAdjust="spacingAndGlyphs" fill="var(--word-solid)">tarrow</text>
      <text class="big-word" x="8" y="406" font-size="92" textLength="460" lengthAdjust="spacingAndGlyphs" fill="var(--word-grey)">tarrow</text>
      <text class="big-word" x="8" y="502" font-size="92" textLength="460" lengthAdjust="spacingAndGlyphs" fill="var(--word-grey)">tarrow</text>
    </svg>
    <div class="flyer__portrait" style="left:155px; top:196px; width:168px; height:290px;" role="img" aria-label="Photo of the session host in a light t-shirt and bead necklace"></div>

    <p class="flyer__line brand" style="top:20px; font-size:30px;">tarrow</p>
    <p class="flyer__line brand-sub" style="top:54px; font-size:13px;">Tarrow Guidance Alliance</p>
    <p class="flyer__line event-title" style="top:87px; font-size:15px;">Tarrow Flow &amp; Hum Unwind Session -</p>
    <p class="flyer__line event-mix" style="top:109px; font-size:23px;">Bayline Mix</p>
    <p class="flyer__line event-date" style="top:144px; font-size:14px;">Wednesday, April 20 | 7PM - 9PM</p>
    <p class="flyer__line event-venue" style="top:170px; font-size:14.5px;"><svg width="10" height="13" viewBox="0 0 10 13" aria-hidden="true"><path d="M5 0C2.2 0 0 2.2 0 5c0 3.6 5 8 5 8s5-4.4 5-8c0-2.8-2.2-5-5-5zm0 7a2 2 0 1 1 0-4 2 2 0 0 1 0 4z" fill="var(--white)"/></svg>Reedhall at Cobbleyard</p>
  </section>

  <!-- Story -->
  <section class="flyer flyer--story">
    <div class="flyer__pattern" role="img" aria-label="Blue mandala line pattern background"></div>
    <svg class="flyer__rings" viewBox="0 0 518 670" aria-hidden="true">
      <g fill="none" stroke="var(--ring)" stroke-width="1.5">
        <ellipse cx="259" cy="450" rx="100" ry="135"/>
        <ellipse cx="259" cy="450" rx="165" ry="195"/>
        <ellipse cx="259" cy="450" rx="235" ry="250"/>
        <ellipse cx="259" cy="450" rx="310" ry="310"/>
      </g>
    </svg>
    <svg class="flyer__words" viewBox="0 0 518 670" aria-hidden="true">
      <text class="big-word" x="8" y="444" font-size="100" textLength="502" lengthAdjust="spacingAndGlyphs" fill="var(--word-solid)">tarrow</text>
      <text class="big-word" x="8" y="556" font-size="100" textLength="502" lengthAdjust="spacingAndGlyphs" fill="var(--word-grey)">tarrow</text>
      <text class="big-word" x="8" y="660" font-size="100" textLength="502" lengthAdjust="spacingAndGlyphs" fill="var(--word-grey)">tarrow</text>
    </svg>
    <div class="flyer__portrait" style="left:155px; top:276px; width:227px; height:400px;" role="img" aria-label="Photo of the session host in a light t-shirt and bead necklace"></div>

    <p class="flyer__line brand" style="top:44px; font-size:40px;">tarrow</p>
    <p class="flyer__line brand-sub" style="top:85px; font-size:16.5px;">Tarrow Guidance Alliance</p>
    <p class="flyer__line event-title" style="top:129px; font-size:18px;">Tarrow Flow &amp; Hum Unwind Session -</p>
    <p class="flyer__line event-mix" style="top:156px; font-size:29px;">Bayline Mix</p>
    <p class="flyer__line event-date" style="top:203px; font-size:18px;">Wednesday, April 20 | 7PM - 9PM</p>
    <p class="flyer__line event-venue" style="top:236px; font-size:19px;"><svg width="11" height="15" viewBox="0 0 10 13" aria-hidden="true"><path d="M5 0C2.2 0 0 2.2 0 5c0 3.6 5 8 5 8s5-4.4 5-8c0-2.8-2.2-5-5-5zm0 7a2 2 0 1 1 0-4 2 2 0 0 1 0 4z" fill="var(--white)"/></svg>Reedhall at Cobbleyard</p>
  </section>

</main>
</body>
</html>
```